Business Card Design for K&R Global

K&R Global designs and manufactures ball valves which are used in Oil & Gas drilling and production.

```html
<!DOCTYPE html>
<html lang="en">
<head>
<meta charset="utf-8">
<title>K&amp;R Global — Business Card</title>
<link rel="stylesheet" href="https://fonts.googleapis.com/css2?family=Open+Sans:wght@400;600;700&display=swap">
<style>
  :root{
    --bg:#2a2623;
    --charcoal:#262626;
    --white:#ffffff;
    --text-soft:#e6e6e6;
    --brand-green:#5a9142;
    --badge:#7d7d7d;
  }
  *{margin:0;padding:0;box-sizing:border-box}
  html,body{width:1200px;height:900px;overflow:hidden}
  body{
    background:var(--bg);
    font-family:"Open Sans",Arial,sans-serif;
    color:var(--white);
    position:relative;
  }
  .card{
    position:absolute;
    width:630px;height:360px;
    border-radius:14px;
    overflow:hidden;
    box-shadow:0 12px 30px rgba(0,0,0,.45);
  }
  .card-front{left:285px;top:60px}
  .card-back{left:285px;top:480px}
  .card-bg{position:absolute;inset:0;width:100%;height:100%}

  /* front */
  .map-backdrop{
    position:absolute;left:120px;top:10px;width:300px;height:190px;
    background:radial-gradient(ellipse at center,rgba(120,160,100,.22),rgba(120,160,100,0) 70%);
  }
  .person{position:absolute;left:34px;top:30px}
  .person-name{font-size:27px;font-weight:700;line-height:1.1}
  .person-title{font-size:17px;font-weight:400;margin-top:4px;color:var(--text-soft)}
  .contact-list{position:absolute;left:36px;top:168px;list-style:none}
  .contact-list li{display:flex;align-items:center;gap:16px;font-size:13px;height:38px;color:var(--text-soft)}
  .contact-list svg{width:18px;height:18px;flex:none}
  .office{
    position:absolute;right:30px;top:162px;text-align:right;
    font-size:13px;line-height:1.4;color:var(--text-soft);
  }
  .office dt{font-weight:700;color:var(--white);margin-top:8px}
  .office dt:first-child{margin-top:0}

  /* back */
  .brand{
    position:absolute;left:0;right:0;top:120px;text-align:center;
  }
  .brand-name{font-size:40px;font-weight:600;color:var(--brand-green)}
  .cert-badge{
    position:absolute;right:56px;top:36px;
    width:48px;height:48px;border-radius:50%;
    background:var(--badge);
  }
  .web-address{
    position:absolute;left:0;right:0;top:272px;text-align:center;
    font-size:25px;font-weight:400;color:var(--text-soft);
  }
</style>
</head>
<body>

<section class="card card-front" aria-label="Card front">
  <svg class="card-bg" viewBox="0 0 630 360" preserveAspectRatio="none" aria-hidden="true">
    <defs>
      <linearGradient id="frontDark" x1="0" y1="0" x2="0" y2="1">
        <stop offset="0" stop-color="#4a4a4a"/>
        <stop offset="1" stop-color="#1f1f1f"/>
      </linearGradient>
      <linearGradient id="frontGreen" x1="0" y1="0" x2="1" y2="1">
        <stop offset="0" stop-color="#4d7a3a"/>
        <stop offset="1" stop-color="#2c5022"/>
      </linearGradient>
      <linearGradient id="swoosh" x1="0" y1="0" x2="0" y2="1">
        <stop offset="0" stop-color="#ffffff"/>
        <stop offset=".5" stop-color="#bdbdbd"/>
        <stop offset="1" stop-color="#7a7a7a"/>
      </linearGradient>
    </defs>
    <rect width="630" height="360" fill="url(#frontDark)"/>
    <path d="M0 0 H520 C440 90 330 230 290 360 H0 Z" fill="url(#frontGreen)"/>
    <path d="M520 0 H536 C450 95 345 235 306 360 H290 C330 230 440 90 520 0 Z" fill="url(#swoosh)"/>
  </svg>
  <div class="map-backdrop" role="img" aria-label="Faint world map backdrop"></div>

  <header class="person">
    <h1 class="person-name">Daniel Whitaker</h1>
    <p class="person-title">Operations Manager</p>
  </header>

  <ul class="contact-list">
    <li>
      <svg viewBox="0 0 24 24" aria-hidden="true"><path fill="#e6e6e6" d="M6.6 10.8a15 15 0 0 0 6.6 6.6l2.2-2.2c.3-.3.7-.4 1-.2 1.1.4 2.3.6 3.6.6.6 0 1 .4 1 1V20c0 .6-.4 1-1 1A17 17 0 0 1 3 4c0-.6.4-1 1-1h3.5c.6 0 1 .4 1 1 0 1.3.2 2.5.6 3.6.1.3 0 .7-.2 1z"/></svg>
      (555) 214-7730
    </li>
    <li>
      <svg viewBox="0 0 24 24" aria-hidden="true"><rect x="3" y="5" width="18" height="14" rx="1" fill="none" stroke="#e6e6e6" stroke-width="1.8"/><path d="M3 6l9 7 9-7" fill="none" stroke="#e6e6e6" stroke-width="1.8"/></svg>
      daniel@krvalve.com
    </li>
    <li>
      <svg viewBox="0 0 24 24" aria-hidden="true"><circle cx="12" cy="12" r="9" fill="none" stroke="#e6e6e6" stroke-width="1.6"/><ellipse cx="12" cy="12" rx="4" ry="9" fill="none" stroke="#e6e6e6" stroke-width="1.4"/><path d="M3 12h18M5 7h14M5 17h14" stroke="#e6e6e6" stroke-width="1.2"/></svg>
      www.krvalve.com
    </li>
  </ul>

  <dl class="office">
    <dt>Fax No</dt>
    <dd>(555) 214-7731</dd>
    <dt>Mailing address</dt>
    <dd>P.O. Box 418<br>Fenwick, LA 70600</dd>
    <dt>Physical address</dt>
    <dd>2280 Harbor Bend Hwy<br>Larkspur, LA 70611</dd>
  </dl>
</section>

<section class="card card-back" aria-label="Card back">
  <svg class="card-bg" viewBox="0 0 630 360" preserveAspectRatio="none" aria-hidden="true">
    <defs>
      <linearGradient id="backDark" x1="0" y1="0" x2="0" y2="1">
        <stop offset="0" stop-color="#4a4a4a"/>
        <stop offset="1" stop-color="#232323"/>
      </linearGradient>
      <linearGradient id="backGreen" x1="0" y1="0" x2="0" y2="1">
        <stop offset="0" stop-color="#4a7a38"/>
        <stop offset="1" stop-color="#2f5424"/>
      </linearGradient>
    </defs>
    <rect width="630" height="360" fill="url(#backDark)"/>
    <rect y="250" width="630" height="110" fill="url(#backGreen)"/>
  </svg>

  <div class="brand">
    <span class="brand-name">K&amp;R Global</span>
  </div>

  <div class="cert-badge" role="img" aria-label="Certification badge"></div>

  <p class="web-address">www.krvalve.com</p>
</section>

</body>
</html>
```